KVL cards

Design business cards for renamed business. Korvane Lighting Limited is a leading contract designer of electronic lighting products sepcialising in LED lighting. Need a design that is simple but clear please. Cards for two persons requried.

Target Market(s)

Professional and technical

Industry/Entity Type

Business

Font styles to use
Sans Serif
Other font styles liked:
• tahoma

Colors
ffcf3e

```html
<!DOCTYPE html>
<html lang="en">
<head>
<meta charset="utf-8">
<title>KVL Business Card</title>
<link rel="stylesheet" href="https://fonts.googleapis.com/css2?family=Cinzel:wght@400;600&family=Crimson+Text:wght@400;600&display=swap">
<style>
  :root {
    --page-bg: #e9e6e1;
    --card-bg: #2b2b2c;
    --card-bg-light: #353536;
    --gold: #ffcf3e;
    --gold-glow: rgba(255, 207, 62, 0.35);
  }
  * { margin: 0; padding: 0; box-sizing: border-box; }
  html, body {
    width: 1200px;
    height: 1008px;
    overflow: hidden;
    background: var(--page-bg);
  }
  .stage {
    width: 1200px;
    height: 1008px;
    display: flex;
    align-items: center;
    justify-content: center;
  }
  .card {
    position: relative;
    width: 1050px;
    height: 600px;
    background: linear-gradient(135deg, var(--card-bg-light) 0%, var(--card-bg) 60%, #262627 100%);
    box-shadow: 0 10px 30px rgba(0, 0, 0, 0.25);
    color: var(--gold);
    overflow: hidden;
  }
  .company-name {
    position: absolute;
    left: 62px;
    top: 180px;
    max-width: 640px;
    white-space: nowrap;
    font-family: "Cinzel", serif;
    font-weight: 600;
    font-size: 37px;
    line-height: 1;
    letter-spacing: 0.5px;
    text-shadow: 0 0 6px var(--gold-glow);
  }
  .person {
    position: absolute;
    right: 62px;
    top: 96px;
    text-align: right;
    font-family: "Crimson Text", serif;
    white-space: nowrap;
  }
  .person-name {
    font-size: 40px;
    line-height: 1.1;
  }
  .person-role {
    font-size: 27px;
    line-height: 1.25;
  }
  .divider {
    position: absolute;
    left: 0;
    right: 0;
    top: 242px;
    height: 3px;
    background: var(--gold);
    box-shadow: 0 0 10px var(--gold-glow);
  }
  .contact-list {
    position: absolute;
    left: 62px;
    top: 318px;
    list-style: none;
    font-family: "Crimson Text", serif;
    font-size: 42px;
  }
  .contact-item {
    display: flex;
    align-items: center;
    gap: 24px;
    height: 78px;
    white-space: nowrap;
  }
  .contact-icon {
    width: 36px;
    height: 36px;
    flex: none;
  }
</style>
</head>
<body>
<main class="stage">
  <article class="card">
    <h1 class="company-name">KORVANE LIGHTING LIMITED</h1>
    <div class="person">
      <p class="person-name">Your Name</p>
      <p class="person-role">Designation</p>
    </div>
    <div class="divider"></div>
    <ul class="contact-list">
      <li class="contact-item">
        <svg class="contact-icon" viewBox="0 0 24 24" aria-hidden="true">
          <path fill="#ffcf3e" d="M6.6 2.5c.6-.3 1.3-.1 1.6.5l1.9 3.4c.3.6.2 1.2-.3 1.6L8.4 9c.9 2.4 2.6 4.4 4.9 5.7l1.3-1.3c.4-.5 1.1-.6 1.6-.3l3.4 1.9c.6.3.8 1 .5 1.6l-1.1 2.3c-.4.8-1.3 1.3-2.2 1.1C9.6 18.7 4.7 13.3 3.6 6.1c-.1-.9.3-1.8 1.1-2.3z"/>
        </svg>
        <span>+44 000 0097</span>
      </li>
      <li class="contact-item">
        <svg class="contact-icon" viewBox="0 0 24 24" aria-hidden="true">
          <rect x="2" y="5" width="20" height="14" fill="#ffcf3e"/>
          <path d="M2.5 5.5 12 13l9.5-7.5" fill="none" stroke="#2b2b2c" stroke-width="1.6"/>
        </svg>
        <span>mail@mail.com</span>
      </li>
      <li class="contact-item">
        <svg class="contact-icon" viewBox="0 0 24 24" aria-hidden="true">
          <circle cx="12" cy="12" r="10" fill="#ffcf3e"/>
          <g fill="none" stroke="#2b2b2c" stroke-width="1.3">
            <ellipse cx="12" cy="12" rx="4.2" ry="10"/>
            <line x1="12" y1="2" x2="12" y2="22"/>
            <line x1="2" y1="12" x2="22" y2="12"/>
            <path d="M4 7h16M4 17h16"/>
          </g>
        </svg>
        <span>www.website.com</span>
      </li>
    </ul>
  </article>
</main>
</body>
</html>
```